Buch-/eBook-Cover für einen Elternratgeber
Zielgruppe
Buch: Elternratgeber
Titel: Zahlen fühlen
Untertitel: Deinem Kind den richtigen Umgang beibringen
Wir sind der ULM Verlag und suchen ein passendes Cover für unseren neuen Elternratgeber. Mit diesem Buch möchten wir Eltern unterstützen, ihren Kindern einen guten und verantwortungsvollen Umgang mit Geld zu vermitteln.
Anforderungen an das Cover-Design:
Bitte keinen Comicstil
Das Buch richtet sich an Eltern (nicht kindlich oder verspielt gestalten)
Keine direkte Darstellung von Geld (z. B. keine Münzen, Geldscheine, Sparschweine usw.)
Ob mit oder ohne Personen auf dem Cover: sind wir offen
Farbwahl und Bildsprache: gerne seriös, ansprechend und modern
Wir sind gespannt auf kreative und professionelle Vorschläge!
E-Book E-Book"
Das Design darf nicht zu überladen sein.

```html
<!DOCTYPE html>
<html lang="de">
<head>
<meta charset="utf-8">
<title>Zahlen fühlen – Elternratgeber</title>
<link rel="stylesheet" href="https://fonts.googleapis.com/css2?family=Montserrat:wght@600&family=Source+Sans+3:wght@400;500&display=swap">
<style>
  :root {
    --ink: #1c2358;
    --ink-dark: #151a2e;
    --mist: #e8e8ec;
    --fog: #c9ccd3;
    --teal: #4fc6d8;
    --pink: #f08ac0;
    --lime: #d9e88a;
    --orange: #e8823c;
    --green: #5f9a3a;
    --navy: #18304a;
    --magenta: #b8235e;
  }
  * { margin: 0; padding: 0; box-sizing: border-box; }
  html, body { width: 750px; height: 1200px; overflow: hidden; background: #fff; }
  .cover {
    position: relative;
    width: 750px;
    height: 1200px;
    overflow: hidden;
    background: var(--mist);
  }
  .cover-artwork {
    position: absolute;
    inset: 0;
    background:
      radial-gradient(ellipse 140px 260px at 120px 560px, rgba(79,198,216,.35), transparent 70%),
      radial-gradient(ellipse 160px 320px at 560px 640px, rgba(240,138,192,.30), transparent 70%),
      radial-gradient(ellipse 120px 200px at 260px 820px, rgba(217,232,138,.35), transparent 70%),
      radial-gradient(ellipse 180px 380px at 420px 420px, rgba(79,198,216,.30), transparent 70%),
      linear-gradient(100deg, #b9bcc4 0%, #cfd2d8 35%, #e6e6ea 65%, #f6f6f7 100%);
  }
  .title {
    position: absolute;
    left: 0;
    top: 0;
    width: 750px;
    height: 620px;
  }
  .title text { font-family: "Montserrat", sans-serif; font-weight: 600; }
  .subtitle {
    position: absolute;
    top: 612px;
    left: 0;
    width: 750px;
    text-align: center;
    font-family: "Source Sans 3", sans-serif;
    font-weight: 500;
    font-size: 38px;
    line-height: 54px;
    color: var(--ink);
  }
  .series-label {
    position: absolute;
    top: 1128px;
    left: 0;
    width: 750px;
    text-align: center;
    font-family: "Source Sans 3", sans-serif;
    font-weight: 400;
    font-size: 22px;
    letter-spacing: 3px;
    color: var(--ink);
  }
</style>
</head>
<body>
<div class="cover">
  <div class="cover-artwork" role="img" aria-label="Abstrakte, weich verschwommene Finanzgrafik mit Liniendiagrammen und Rasterflächen in Grau, Türkis, Rosa und Gelb"></div>

  <svg class="title" viewBox="0 0 750 620" aria-label="Zahlen fühlen">
    <defs>
      <linearGradient id="title-main-fill" x1="0" y1="0" x2="1" y2="0.15">
        <stop offset="0" stop-color="var(--orange)"/>
        <stop offset="0.18" stop-color="var(--green)"/>
        <stop offset="0.35" stop-color="#2a6f78"/>
        <stop offset="0.55" stop-color="var(--navy)"/>
        <stop offset="0.72" stop-color="#1d5f8a"/>
        <stop offset="0.86" stop-color="var(--magenta)"/>
        <stop offset="1" stop-color="#5a1d3e"/>
      </linearGradient>
      <linearGradient id="title-sub-fill" x1="0" y1="0" x2="1" y2="0">
        <stop offset="0" stop-color="var(--ink-dark)"/>
        <stop offset="0.55" stop-color="#16304a"/>
        <stop offset="0.72" stop-color="#1b5f82"/>
        <stop offset="1" stop-color="#3a1838"/>
      </linearGradient>
    </defs>
    <text x="72" y="432" font-size="148" textLength="606" lengthAdjust="spacingAndGlyphs" fill="url(#title-main-fill)">ZAHLEN</text>
    <text x="74" y="583" font-size="112" textLength="594" lengthAdjust="spacing" fill="url(#title-sub-fill)">FÜHLEN</text>
  </svg>

  <p class="subtitle">Deinem Kind den richtigen<br>Umgang beibringen</p>

  <p class="series-label">ELTERNRATGEBER</p>
</div>
</body>
</html>
```